business card for a massage therapy practice named 'Meadow and Willow Massage Studio'

I really need a trendy, yet easy on the eyes business card to complement my logo. Ideally with some gold or rose gold foil work.

My uploaded file of the logo I have in horizontal but I have a vertical version as well. Another color that is used in the website is a blush pink here and there. I'd like to see some trendy tropical leaves in the design.

```html
<!DOCTYPE html>
<html lang="en">
<head>
<meta charset="utf-8">
<title>Meadow and Willow Massage Studio – Business Card</title>
<link href="https://fonts.googleapis.com/css2?family=Crimson+Text:wght@400;700&display=swap" rel="stylesheet">
<style>
  :root {
    --backdrop: #ece8e4;
    --ink: #1b1716;
    --strip: #1f1a1a;
    --taupe: #6b615b;
    --taupe-dark: #4a423e;
    --rose-light: #f6ece4;
    --rose-mid: #e3cdbd;
    --rose-deep: #cfae98;
    --foil: #e6d2bf;
    --text-dark: #2a2421;
  }
  * { box-sizing: border-box; margin: 0; padding: 0; }
  html, body { width: 1200px; height: 891px; overflow: hidden; }
  body {
    background: var(--backdrop);
    font-family: "Crimson Text", Georgia, serif;
    position: relative;
  }
  .card {
    position: absolute;
    left: 340px;
    width: 520px;
    height: 297px;
    overflow: hidden;
    box-shadow: 0 6px 18px rgba(0,0,0,0.18);
    background: linear-gradient(180deg, var(--rose-mid) 0%, var(--rose-light) 30%, var(--rose-deep) 55%, var(--rose-light) 80%, var(--rose-mid) 100%);
  }
  .card--front { top: 120px; }
  .card--back { top: 474px; }

  /* Front side */
  .foliage-band {
    position: absolute;
    left: 10px;
    width: 500px;
    background: radial-gradient(ellipse 60% 70% at 50% 50%, rgba(27,23,22,0.78) 0%, rgba(27,23,22,0.5) 55%, rgba(27,23,22,0.12) 85%, rgba(27,23,22,0) 100%);
  }
  .foliage-band--top { top: 0; height: 120px; }
  .foliage-band--bottom { bottom: 4px; height: 112px; }
  .front-centre {
    position: absolute;
    top: 124px;
    left: 0;
    width: 100%;
    text-align: center;
  }
  .studio-name {
    font-weight: 700;
    color: var(--taupe);
    letter-spacing: 0.5px;
  }
  .front-centre .studio-name { font-size: 20px; line-height: 1.1; }
  .front-centre .studio-name .mark {
    display: inline-block;
    width: 10px; height: 10px;
    border-radius: 50%;
    background: var(--taupe);
    margin-right: 8px;
    vertical-align: middle;
  }
  .tagline {
    margin-top: 4px;
    font-size: 12px;
    font-weight: 700;
    color: var(--text-dark);
  }

  /* Back side */
  .back-panel {
    position: absolute;
    top: 0; left: 0;
    width: 175px; height: 100%;
    background: linear-gradient(160deg, #7a6f68 0%, var(--taupe) 45%, var(--taupe-dark) 100%);
  }
  .back-panel .studio-name {
    position: absolute;
    top: 40px; left: 20px;
    width: 148px;
    font-size: 18px;
    line-height: 1.15;
    color: var(--foil);
  }
  .back-strip {
    position: absolute;
    top: 0; left: 175px;
    width: 60px; height: 100%;
    background: var(--strip);
  }
  .icon {
    position: absolute;
    left: 18px;
    width: 24px; height: 24px;
  }
  .icon--phone { top: 74px; }
  .icon--web { top: 134px; }
  .icon--pin { top: 194px; }
  .contact-list { list-style: none; }
  .contact-list li {
    position: absolute;
    left: 252px;
    font-size: 13px;
    color: var(--text-dark);
    line-height: 24px;
    white-space: nowrap;
  }
  .contact-list .phone { top: 74px; }
  .contact-list .web { top: 134px; }
  .contact-list .address { top: 194px; }
</style>
</head>
<body>

<section class="card card--front" aria-label="Card front">
  <div class="foliage-band foliage-band--top" role="img" aria-label="Black tropical palm and monstera leaf silhouettes"></div>
  <div class="front-centre">
    <p class="studio-name"><span class="mark"></span>Meadow and Willow Massage Studio</p>
    <p class="tagline">We offer Integrative and Therapeutic Massage Therapy</p>
  </div>
  <div class="foliage-band foliage-band--bottom" role="img" aria-label="Black tropical palm and monstera leaf silhouettes"></div>
</section>

<section class="card card--back" aria-label="Card back">
  <div class="back-panel" role="img" aria-label="Embossed tropical leaf pattern in taupe tones">
    <p class="studio-name">Meadow and Willow Massage Studio</p>
  </div>
  <div class="back-strip">
    <svg class="icon icon--phone" viewBox="0 0 24 24" aria-hidden="true">
      <path fill="#f1e6dc" d="M6.6 3.5c.5-.5 1.3-.5 1.7.1l1.9 2.8c.3.5.3 1.1-.1 1.5l-1.3 1.3c.9 2 2.5 3.7 4.5 4.6l1.3-1.3c.4-.4 1-.5 1.5-.1l2.8 1.9c.6.4.6 1.2.1 1.7l-1.6 1.6c-.8.8-2 1.1-3.1.7C9.3 16.6 6.4 13.7 4.8 8.7c-.4-1.1-.1-2.300.7-3.1z"/>
    </svg>
    <svg class="icon icon--web" viewBox="0 0 24 24" aria-hidden="true">
      <g fill="none" stroke="#f1e6dc" stroke-width="1.6">
        <circle cx="12" cy="12" r="9"/>
        <ellipse cx="12" cy="12" rx="4" ry="9"/>
        <line x1="3" y1="12" x2="21" y2="12"/>
        <line x1="5" y1="7" x2="19" y2="7"/>
        <line x1="5" y1="17" x2="19" y2="17"/>
      </g>
    </svg>
    <svg class="icon icon--pin" viewBox="0 0 24 24" aria-hidden="true">
      <path fill="#f1e6dc" d="M12 2a7 7 0 0 0-7 7c0 5 7 13 7 13s7-8 7-13a7 7 0 0 0-7-7zm0 9.5A2.5 2.5 0 1 1 12 6.5a2.5 2.5 0 0 1 0 5z"/>
    </svg>
  </div>
  <ul class="contact-list">
    <li class="phone">530-274-1186</li>
    <li class="web">www.meadowandwillow.com</li>
    <li class="address">2417 Fern Avenue, 210, Riverton, CA, 95620</li>
  </ul>
</section>

</body>
</html>
```